Business Card Design

I need a business card for my resume writing business. I have a logo that Im not keen on anymore so I would like the business card to use my photo instead of a logo. I am for mid career and trades resumes and prefer not to do executive resumes so don't need to aim for exectives. I would like it to be colourful. I like bright sky blue and maybe some pink or purple but primarily bright sky blue. I don't like green and Im keen see a fair bit of white on the card. As I have a photo to go it, it will need to go on a white background.

Target Market(s)

mid range careers. Not executives

Industry/Entity Type

Business

Contact Information for Business Card

Wyn Marchetti
Resume Writer
Clear Path CVs
27 The Lanyard
HARWOOD NSW 2465
wyn@clearpathcvs.com.au
0417362958
www.clearpathcvs.com.au

Requirements
Nice to have
• Maybe colours similar to my website - www.clearpathcvs.com.au but not with any black on it.
Should not have
• No green or dark colours

```html
<!DOCTYPE html>
<html lang="en">
<head>
<meta charset="utf-8">
<title>Clear Path CVs – Business Card</title>
<link rel="stylesheet" href="https://fonts.googleapis.com/css2?family=Open+Sans:wght@600;700&display=swap">
<style>
  :root {
    --sky: #3a9ad6;
    --white: #ffffff;
    --portrait-light: #f3ebe6;
    --portrait-mid: #d9b8a6;
    --portrait-dark: #6e4a3c;
  }
  html, body {
    margin: 0;
    padding: 0;
    overflow: hidden;
    background: var(--white);
  }
  .card {
    position: relative;
    width: 1200px;
    height: 741px;
    overflow: hidden;
    background: var(--white);
    font-family: "Open Sans", Arial, sans-serif;
  }
  .sky-panel {
    position: absolute;
    left: 435px;
    top: 0;
    width: 765px;
    height: 741px;
    background: var(--sky);
  }
  .pointer {
    position: absolute;
    left: 434px;
    top: 95px;
    width: 105px;
    height: 130px;
  }
  .portrait {
    position: absolute;
    left: 0;
    top: 0;
    width: 600px;
    height: 741px;
  }
  .brand-name {
    position: absolute;
    left: 505px;
    top: 150px;
    width: 600px;
    margin: 0;
    text-align: center;
    font-weight: 600;
    font-size: 74px;
    line-height: 1.1;
    color: var(--white);
  }
  .contact {
    position: absolute;
    right: 43px;
    top: 512px;
    margin: 0;
    text-align: right;
    font-weight: 700;
    font-size: 24px;
    line-height: 38.5px;
    color: var(--white);
    font-style: normal;
  }
  .contact span { display: block; }
</style>
</head>
<body>
  <div class="card">
    <div class="sky-panel"></div>
    <svg class="pointer" viewBox="0 0 105 130" aria-hidden="true">
      <polygon points="0,0 105,65 0,130" fill="#ffffff"/>
    </svg>
    <svg class="portrait" viewBox="0 0 600 741" role="img" aria-label="Portrait photo of Wyn Marchetti, smiling, in a white jacket">
      <defs>
        <linearGradient id="portrait-tone" x1="0" y1="0" x2="0" y2="1">
          <stop offset="0" stop-color="#6e4a3c"/>
          <stop offset="0.35" stop-color="#d9b8a6"/>
          <stop offset="0.6" stop-color="#f3ebe6"/>
          <stop offset="1" stop-color="#ffffff"/>
        </linearGradient>
      </defs>
      <path d="M0 741 L0 392 C40 374 80 362 100 352 C78 250 92 78 215 67 C335 58 362 222 346 340 C392 368 432 402 452 442 C500 522 560 640 585 741 Z" fill="url(#portrait-tone)"/>
    </svg>
    <p class="brand-name">Clear Path CVs</p>
    <address class="contact">
      <span>Wyn Marchetti Resume Writer Clear Path CVs</span>
      <span>27 The Lanyard HARWOOD NSW 2465</span>
      <span>wyn@clearpathcvs.com.au</span>
      <span>0417362958</span>
      <span>www.clearpathcvs.com.au</span>
    </address>
  </div>
</body>
</html>
```